Design a Retail Box for Industrial Welding Helmets

We are excited to launch a design contest for our product's new retail packaging.
The products are 2 welding helmets.
Product 1 is Brontal helmet and product 2 is Veltrix helmet.
We are seeking for :
A) 1 main design of the box with minor adjustments for the 2 different models (Brontal and Veltrix)
B) 1 design for the sticker of Brontal (font)
C)1 design for the sticker of Veltrix (font)
Attached you will find:
1)Brand logo
2)Reference of welding wire packaging
3)Reference of welding torch packaging
4)Photo of Brontal model
5)Data of Brontal model to be included
6)Photo of Veltrix model
7)Data of Veltrix model to be included
8)Dieline Template of the box in .ai and .jpg
9)Vectors for the different uses of the helmets
Your design should reflect our brand and communicate the product's value while standing out on retail shelves.
The winner will be selected based on creativity, brand alignment, and overall design aesthetics.
We look forward to seeing your creative concepts.
Target Market(s)
Industrial and Retail
Industry/Entity Type
Welding, Retail, Hardware
Colors
Designer to choose colors to be used in the design.
Look and feel
Each slider illustrates characteristics of the customer's brand and the style your logo design should communicate.

```html
<!DOCTYPE html>
<html lang="en">
<head>
<meta charset="utf-8">
<title>Korvan Welding Helmet – Retail Box Fronts</title>
<link rel="stylesheet" href="https://fonts.googleapis.com/css2?family=Black+Ops+One&family=Montserrat:wght@500;700;800&display=swap">
<style>
  :root {
    --stage: #000000;
    --box-dark: #131418;
    --box-mid: #1c1e24;
    --text-light: #d9dadd;
    --text-muted: #9a9ca3;
    --mark-grey: #c4c5c8;
    --white: #ffffff;
    --brontal-accent: #3fa6c6;
    --brontal-band: #2d7790;
    --brontal-glow: #1f4f63;
    --brontal-deep: #10303d;
    --veltrix-accent: #8246d0;
    --veltrix-band: #5b2f92;
    --veltrix-glow: #3d2466;
    --veltrix-deep: #241540;
  }
  * { margin: 0; padding: 0; box-sizing: border-box; }
  html, body {
    width: 1200px; height: 674px; overflow: hidden;
    background: var(--stage);
    font-family: "Montserrat", Arial, sans-serif;
  }
  .canvas { position: relative; width: 1200px; height: 674px; }

  .box-front {
    position: absolute; top: 105px;
    width: 300px; height: 460px;
    overflow: hidden;
    background: linear-gradient(180deg, var(--box-mid) 0%, var(--box-dark) 60%, #0c0d10 100%);
  }
  .box-front--brontal { left: 186px; --accent: var(--brontal-accent); --band: var(--brontal-band); --glow: var(--brontal-glow); --deep: var(--brontal-deep); }
  .box-front--veltrix { left: 714px; --accent: var(--veltrix-accent); --band: var(--veltrix-band); --glow: var(--veltrix-glow); --deep: var(--veltrix-deep); }

  .brand-header {
    position: absolute; top: 20px; left: 0; width: 100%;
    text-align: center;
  }
  .brand-header__name {
    display: block;
    font-weight: 700; font-size: 22px; letter-spacing: 4px;
    color: var(--accent);
  }
  .brand-header__model {
    display: block; margin-top: 8px;
    font-family: "Black Ops One", "Arial Black", sans-serif;
    font-size: 11px; letter-spacing: 1px;
    color: var(--accent);
    text-transform: uppercase;
  }

  .brand-emblem {
    position: absolute; top: 120px; left: 34px;
    display: flex; flex-direction: column; align-items: flex-start; gap: 14px;
  }
  .brand-emblem__square {
    width: 78px; height: 78px;
    background: var(--mark-grey);
  }
  .brand-emblem__name {
    font-weight: 700; font-size: 20px; letter-spacing: 3px;
    color: var(--mark-grey);
  }

  .helmet-photo {
    position: absolute; top: 92px; right: 0;
    width: 162px; height: 192px;
    border-radius: 70px 0 0 30px;
    background:
      radial-gradient(ellipse 55% 45% at 62% 52%, var(--accent) 0%, var(--glow) 45%, transparent 85%),
      linear-gradient(160deg, var(--glow) 0%, var(--deep) 70%, #0e0f13 100%);
  }

  .wordmark {
    position: absolute; top: 294px; left: 28px;
    display: flex; align-items: center; gap: 10px;
  }
  .wordmark__name {
    font-weight: 500; font-size: 30px; letter-spacing: 5px;
    color: var(--text-light);
  }
  .wordmark__product {
    font-weight: 800; font-size: 12px; line-height: 1.05;
    letter-spacing: 0.5px;
    color: var(--text-muted);
    text-transform: uppercase;
  }

  .model-name {
    position: absolute; top: 335px; left: 0; width: 100%;
    text-align: center;
    font-family: "Black Ops One", "Arial Black", sans-serif;
    font-weight: 400;
    font-size: 48px; letter-spacing: 1px;
    color: var(--accent);
    text-transform: uppercase;
  }

  .tagline-band {
    position: absolute; top: 398px; left: 0; width: 100%; height: 22px;
    background: var(--band);
    display: flex; align-items: center; justify-content: center;
    font-weight: 700; font-size: 11px;
    color: var(--white);
  }

  .base-glow {
    position: absolute; bottom: 0; left: 0; width: 100%; height: 40px;
    background: radial-gradient(ellipse 70% 100% at 50% 100%, var(--glow) 0%, transparent 80%);
  }
</style>
</head>
<body>
<main class="canvas">

  <section class="box-front box-front--brontal" aria-label="Brontal box front">
    <header class="brand-header">
      <span class="brand-header__name">KORVAN</span>
      <span class="brand-header__model">Brontal</span>
    </header>
    <div class="brand-emblem">
      <span class="brand-emblem__square"></span>
      <span class="brand-emblem__name">KORVAN</span>
    </div>
    <div class="helmet-photo" role="img" aria-label="Photo of the Brontal welding helmet in blue light"></div>
    <div class="wordmark">
      <span class="wordmark__name">KORVAN</span>
      <span class="wordmark__product">Welding<br>Helmet</span>
    </div>
    <h2 class="model-name">Brontal</h2>
    <p class="tagline-band">The choice of experts.</p>
    <div class="base-glow"></div>
  </section>

  <section class="box-front box-front--veltrix" aria-label="Veltrix box front">
    <header class="brand-header">
      <span class="brand-header__name">KORVAN</span>
      <span class="brand-header__model">Veltrix</span>
    </header>
    <div class="brand-emblem">
      <span class="brand-emblem__square"></span>
      <span class="brand-emblem__name">KORVAN</span>
    </div>
    <div class="helmet-photo" role="img" aria-label="Photo of the Veltrix welding helmet in purple light"></div>
    <div class="wordmark">
      <span class="wordmark__name">KORVAN</span>
      <span class="wordmark__product">Welding<br>Helmet</span>
    </div>
    <h2 class="model-name">Veltrix</h2>
    <p class="tagline-band">The choice of experts.</p>
    <div class="base-glow"></div>
  </section>

</main>
</body>
</html>
```